BRANDING MOODBOARD - TEST PROJECT

Description in link:
https://www.filecrate-example.net/s/k27384wqpz51mvt/PERCH%20Moodboard%20Project.pdf?dl=0

You'll notice that most of my images are a little dark / edgy or dramatic & gripping. An unplanned pregnancy elicits a lot of emotion including but not limited to fear, angst, uncertainty, shame, pressure, etc. My hope is that my materials will display a strong contrast between the dark (fears) and light (hope). The young women who will be part of this program will have a comprehensive support system that will help to strengthen, encourage and prepare her for the road ahead - whether she choses to go the route of becoming a single mother or whether she decides that placing the baby up for adoption is best. Either way, she will receive the utmost care, love, and compassion for her courage to see the pregnancy through to full-term.

Our motto is "Sow Dawn". Not only is this young woman "bringing life" into the world, but the Host Families and Mentors will also be "bringing life" to the young mother by giving her hope beyond this season.

Target Market(s)

Females ages 18-24 who are unwed and find themselves unexpectedly pregnant who lack the support they need.

Industry/Entity Type

Non Profit

Font styles to use
Serif
Sans Serif
Other font styles liked:
• I've been using Anchorage for Perch - and I'm indifferent re: Montserrat

Colors
fee3d4
fbd4d5
feeeee
fff5ef
f59195

Requirements
Must have
• This is just a moodboard project, however the winner will be awarded numerous projects to follow - each with their own budgets, creative briefs, etc. Future projects to include:
• - Logo clean-up. The current mechanical files are poor (combo .eps and .png) I want all-vector artwork for scalability.
• - Stationery System (letterhead, envelope, business card, thank you note, simple folder for presentation materials)
• - Basic Website (Likely Pagely - est. 10 pages) limited functionality, no ecommerce, no special features.
• - PowerPoint (or similar program) Template
• - One-Sheets : single page presentation materials (copy-heavy docs).
• - Brochure
• - Pitch Book (likely Quill, or Lantern Foldworks or something similar)
• - Icon System.
• * If a bird is used it must be a swallow. The Bible verse Psalm 84.3 is an essential part of the company's name.
• * I particularly like hand-drawn elements as demonstrated by the current bird in the logo. They're very human and "not perfect".
• * Generally I'm a huge fan of simple and clean. Not crazy or over the top modern/contemporary though. I just love lots of white space and simple, organic / natural feeling materials. For that reason I've chosen what I think are fairly muted / earth-tones for the soft pinks.
• * I like monochromatic and muted color palettes. I'm open to suggestions if the designer would like to make alternate recommendations to the colors.
• * Finally, I'm not married to the logo. If someone has another version that they feel strongly about I'm completely open to considering. At one point I was playing with a "scribbled" nest in the logo as opposed to the bird. (attached in image files below)
Nice to have
• I particularly liked image "Perch-5". I sort of feel like this image says it all. The words in her tatoo are gripping and poignant. It's important that the entire tone of the brochure not be "dark, fearful or uncertain" -- but that we turn such an uncertain season as an unplanned pregnancy into something hopeful and full of light, optimism and peace.
• I'm not crazy about my current "complimentary" typefaces - especially Bebas Neue. I'd love to see some alternate type systems ... demonstrating how headlines and body copy would be treated in fonts that play nice with the logo.
• I'm also not married to Anchorage. I liked the kind of retro / vintage thing, but it's definitely not necessary.
Should not have
• Do not include any material or messaging pertaining to "pro-choice". This is a distinctly pro-life and pro-love initiative.

```html
<!DOCTYPE html>
<html lang="en">
<head>
<meta charset="utf-8">
<title>Perch – Business Card</title>
<link href="https://fonts.googleapis.com/css2?family=Roboto:wght@300;400;500&display=swap" rel="stylesheet">
<style>
  :root {
    --backdrop: #2a2a2a;
    --card: #ffffff;
    --blush: #d8bcad;
    --blush-soft: #e9d6cc;
    --ink-grey: #8c8c8c;
  }
  * { margin: 0; padding: 0; box-sizing: border-box; }
  html, body { width: 1200px; height: 1040px; overflow: hidden; }
  body {
    background: var(--backdrop);
    font-family: "Roboto", Helvetica, Arial, sans-serif;
    position: relative;
  }
  .card {
    position: absolute;
    left: 250px;
    width: 700px;
    height: 400px;
    background: var(--card);
    box-shadow: 0 6px 18px rgba(0,0,0,0.45);
  }
  .card--front { top: 70px; }
  .card--back { top: 570px; }

  .swallow-art {
    position: absolute;
    display: block;
  }
  .card--front .swallow-art { right: 30px; top: 24px; width: 330px; height: 200px; }
  .card--back .swallow-art { left: 470px; top: 186px; width: 120px; height: 70px; }

  .wordmark {
    color: var(--blush);
    font-weight: 300;
    letter-spacing: 1px;
    line-height: 1;
  }
  .card--front .wordmark {
    position: absolute;
    left: 40px;
    top: 112px;
    font-size: 104px;
  }
  .card--back .wordmark {
    position: absolute;
    left: 0; right: 0;
    top: 150px;
    text-align: center;
    font-size: 92px;
    padding-right: 40px;
  }

  .contact {
    position: absolute;
    left: 108px;
    top: 250px;
    color: var(--ink-grey);
    font-size: 14px;
    line-height: 1.35;
  }
  .contact__name {
    color: var(--blush);
    font-weight: 500;
    font-size: 19px;
    letter-spacing: 0.5px;
  }
  .contact__role {
    font-size: 16px;
    font-weight: 300;
    margin-bottom: 12px;
  }
  .contact__address { margin-bottom: 10px; }
</style>
</head>
<body>

  <section class="card card--front">
    <svg class="swallow-art" role="img" aria-label="Hand-sketched swallow in flight, wings spread" viewBox="0 0 330 200">
      <defs>
        <linearGradient id="swallowTone" x1="0" y1="0" x2="1" y2="1">
          <stop offset="0" stop-color="#e6d2c7"/>
          <stop offset="1" stop-color="#d8bcad"/>
        </linearGradient>
      </defs>
      <rect width="330" height="200" fill="url(#swallowTone)" rx="6"/>
    </svg>

    <div class="wordmark">Perch</div>

    <div class="contact">
      <div class="contact__name">DANIEL HALE</div>
      <div class="contact__role">CEO/FOUNDER</div>
      <div class="contact__address">2140 Willowmere Road<br>Fairbrook, Oregon 97215</div>
      <div class="contact__lines">P. 503 281 4176 C. 503 917 2045<br>E. daniel@perchhome.org W. www.perchhome.org</div>
    </div>
  </section>

  <section class="card card--back">
    <div class="wordmark">Perch</div>
    <svg class="swallow-art" role="img" aria-label="Small hand-sketched swallow in flight" viewBox="0 0 120 70">
      <rect width="120" height="70" fill="var(--blush-soft)" rx="4"/>
    </svg>
  </section>

</body>
</html>
```